Green Ammonia PowerPoint Slides

Hi KORU Designs. You did a PowerPoint project for us previously (As BelvaGas LLC) which we very much liked and are looking for something similar in terms of design.

VerdoMolix LLC is a project development company that develops green ammonia projects. Our concept converts renewable energy from wind, solar, hydro and geothermal power sources into ammonia which can be transported by land or sea to be used as a carbon free fuel source.

We need a professional looking design for the attached PowerPoint file. The attached PowerPoint file includes the written content for each of the slides. Designers’ final product should include all the written content and be a final product for presenting to our clients with little to no more editing required.

Designer should use the graphics attached and colors as inspiration for the design. Adjacent to the logo and where used in headings it should read: “A VerdoMolix LLC Project”. Designer is free to use/modify the logo and colors however they feel provides a more interesting design and aesthetic.

Designer should include graphics, tables and charts to better present the information where it is appropriate.

The previous design you developed for us used the ETHNOCENTRIC RG font for titles, which we liked, though you are free to use any font at your discretion as long as it is free to download.

```html
<!DOCTYPE html>
<html lang="en">
<head>
<meta charset="utf-8">
<title>Green Ammonia PowerPoint Slides</title>
<link rel="stylesheet" href="https://fonts.googleapis.com/css2?family=Orbitron:wght@700;900&family=Open+Sans:wght@400;600;700;800&display=swap">
<style>
:root{
  --stage:#484848;
  --navy:#0b2a52;
  --navy-deep:#03254a;
  --blue:#1d5fbf;
  --teal:#2fa7a0;
  --green:#5cc24a;
  --lime:#7dd34d;
  --ink:#1a1a1a;
  --paper:#ffffff;
  --mist:#e6e6e6;
}
*{margin:0;padding:0;box-sizing:border-box}
html,body{width:693px;height:1200px;overflow:hidden}
body{background:var(--stage);position:relative;font-family:"Open Sans",Arial,sans-serif;color:var(--ink)}
.slide{position:absolute;left:36px;width:616px;height:346px;overflow:hidden;background:var(--paper);box-shadow:0 3px 8px rgba(0,0,0,.45)}
.slide--cover{top:48px}
.slide--intro{top:417px}
.slide--proposition{top:788px}

/* cover */
.cover-photo{position:absolute;inset:0;background:linear-gradient(115deg,#1750c4 0%,#1f8fbd 35%,#3cbf86 65%,#6ed24a 100%)}
.cover-mark{position:absolute;top:30px;left:0;right:0;display:flex;justify-content:center;align-items:center;gap:6px;color:var(--paper);font-family:"Orbitron",sans-serif;font-weight:700;font-size:11px;letter-spacing:1px}
.cover-mark .dot{width:22px;height:22px;border-radius:50%;background:var(--paper)}
.cover-title{position:absolute;left:0;right:0;text-align:center;color:var(--paper);font-family:"Orbitron",sans-serif;font-weight:900;line-height:1}
.cover-title--a{top:93px;font-size:38px}
.cover-title--name{top:141px;font-size:37px;letter-spacing:-.5px}
.cover-band{position:absolute;left:110px;top:184px;width:394px;height:48px;background:var(--navy-deep);display:flex;align-items:center;justify-content:center;color:var(--paper);font-family:"Orbitron",sans-serif;font-weight:900;font-size:38px;letter-spacing:2px}
.cover-sheet{position:absolute;top:264px;left:0;right:0;text-align:center;color:var(--paper);font-family:"Orbitron",sans-serif;font-weight:900;font-size:18px;letter-spacing:1px}
.cover-meta{position:absolute;top:289px;left:0;right:0;text-align:center;color:var(--paper);font-weight:600;font-size:13px;line-height:17px;text-decoration:underline}

/* content slides */
.slide-head{position:absolute;left:20px;top:17px;display:flex;align-items:center}
.head-dot{width:34px;height:34px;border-radius:50%;background:linear-gradient(180deg,var(--blue),var(--green))}
.head-band{position:absolute;left:43px;top:8px;width:320px;height:36px;background:linear-gradient(90deg,var(--mist),rgba(230,230,230,0))}
.slide-title{position:absolute;left:70px;top:22px;font-family:"Orbitron",sans-serif;font-weight:700;font-size:28px;color:var(--navy);line-height:36px;white-space:nowrap}
.slide-subtitle{position:absolute;left:66px;top:63px;font-family:"Orbitron",sans-serif;font-weight:700;font-size:19px;color:var(--navy);white-space:nowrap}
.tag{position:absolute;right:0;top:25px;width:137px;height:19px;background:var(--green);border-radius:10px 0 0 10px;color:var(--paper);font-family:"Orbitron",sans-serif;font-weight:700;font-size:10px;line-height:19px;padding-left:8px}
.points{position:absolute;list-style:none}
.points li{position:relative}
.points li::before{content:"";position:absolute;border-radius:50%;background:linear-gradient(180deg,var(--blue) 50%,var(--green) 50%)}
.points--intro{left:53px;top:82px;width:540px;display:flex;flex-direction:column;gap:13px;font-size:11.2px;line-height:13px}
.points--intro li::before{left:-26px;top:2px;width:14px;height:14px}
.points--prop{left:49px;top:105px;width:545px;display:flex;flex-direction:column;gap:9.5px;font-size:8.9px;line-height:11px}
.points--prop li::before{left:-24px;top:1px;width:9px;height:9px}
.points--prop b{font-weight:800}
.slide-foot{position:absolute;left:0;right:0;bottom:0;height:32px;background:linear-gradient(90deg,var(--navy-deep) 0%,#1c6a80 40%,#4aa852 75%,var(--lime) 100%)}
.foot-url{position:absolute;left:24px;top:0;line-height:32px;color:var(--paper);font-weight:700;font-size:12.5px}
.foot-page{position:absolute;right:20px;top:4px;width:25px;height:25px;border-radius:50%;background:var(--navy-deep);color:var(--paper);font-weight:700;font-size:12px;line-height:25px;text-align:center}

.caption{position:absolute;top:1155px;left:0;right:0;text-align:center;color:#e8e8e8;font-size:19px}
</style>
</head>
<body>

<section class="slide slide--cover">
  <div class="cover-photo" role="img" aria-label="Photo of wind turbines on hills and an engineer in a hard hat holding a tablet, tinted blue to green"></div>
  <div class="cover-mark"><span class="dot"></span>VERDOMOLIX</div>
  <h1 class="cover-title cover-title--a">A</h1>
  <div class="cover-title cover-title--name">VERDOMOLIX LLC</div>
  <div class="cover-band">PROJECT</div>
  <div class="cover-sheet">COVERSHEET HERE</div>
  <div class="cover-meta">Cove Ltd - VerdoMolix Introduction<br>Date: XX/XX/XXXX</div>
</section>

<section class="slide slide--intro">
  <div class="head-band"></div>
  <div class="slide-head"><span class="head-dot"></span></div>
  <h2 class="slide-title">Introduction</h2>
  <div class="tag">VERDOMOLIX LLC</div>
  <ul class="points points--intro">
    <li>We are VerdoMolix, experienced energy project developers who have come together with the intent of developing opportunities in North America for the production and export of green energy.</li>
    <li>Our concept converts renewable energy; wind/solar/hydro/geothermal into ammonia, the carrier for hydrogen, which can then be transported internationally to meet the accelerating demand for green renewable power generation.</li>
    <li>We are currently in the concept development stage and are looking at ammonia export from Oregon, Alaska and Texas, and have concluded that the opportunities from Texas are preferable to those on the West Coast.</li>
    <li>We have leveraged our contacts within the LNG market and have established the necessary relationship with a key Japanese buyer who has confirmed interest in base load take off.</li>
    <li>Today we present our high-level concept for developing an ammonia export project in Texas with the goal of furthering conversations with regards your appetite for partnering.</li>
  </ul>
  <footer class="slide-foot"><span class="foot-url">WWW.BELVAGAS.COM</span><span class="foot-page">01</span></footer>
</section>

<section class="slide slide--proposition">
  <div class="head-band"></div>
  <div class="slide-head"><span class="head-dot"></span></div>
  <h2 class="slide-title">The Proposition</h2>
  <div class="slide-subtitle">Why Hydrogen and Green Ammonia?</div>
  <div class="tag">VERDOMOLIX LLC</div>
  <ul class="points points--prop">
    <li><b>It’s unique</b> - Hydrogen is the only fully renewable fuel by which large quantities of energy can be efficiently transported internationally.</li>
    <li><b>It has a proven safety record</b> - While hydrogen has inherent safety issue, synthesis with nitrogen into ammonia enables transport via the established international network of large ocean-going bulk carriers.</li>
    <li><b>It’s green</b> - When Ammonia is re-converted back into electricity via thermal power production there is no CO2 released, catalyst technologies will mean only nitrogen and water are emitted.</li>
    <li><b>The color difference</b> – Grey ammonia is currently produced using hydrogen derived from natural gas, blue ammonia is grey ammonia with carbon sequestration added, neither are green or sustainable. Green Ammonia utilizes renewable electricity to produce hydrogen via electrolysis, this is then combined with nitrogen produced from air via liquefaction. The only emission is oxygen, also a valuable bi-product.</li>
    <li><b>Its power friendly</b> – Ammonia synthesis requires low power as the exothermic reaction generates steam which in turn generates power to run the ammonia facility.</li>
    <li><b>Technology readiness</b> – Industrial scale modular electrolizers are market ready.</li>
  </ul>
  <footer class="slide-foot"><span class="foot-url">WWW.BELVAGAS.COM</span><span class="foot-page">02</span></footer>
</section>

<p class="caption">Green Ammonia PowerPoint Slides</p>

</body>
</html>
```